Oil and Gas Exploration and Production company needs a business card design

We need a business card design using our logo and colors in the logo. We want a mainstream design.

```html
<!DOCTYPE html>
<html lang="en">
<head>
<meta charset="utf-8">
<title>Corra Oil &amp; Gas – Business Card</title>
<link rel="stylesheet" href="https://fonts.googleapis.com/css2?family=Mulish:wght@400;500;800&display=swap">
<style>
  :root {
    --backdrop: #f2eff5;
    --card: #ffffff;
    --cream: #f8f1e6;
    --gold: #c8962d;
    --ink: #111111;
    --text: #222222;
    --white: #ffffff;
  }
  * { margin: 0; padding: 0; box-sizing: border-box; }
  html, body {
    width: 1200px;
    height: 919px;
    overflow: hidden;
    background: var(--backdrop);
    font-family: "Mulish", sans-serif;
  }
  .business-card {
    position: absolute;
    left: 100px;
    top: 140px;
    width: 1000px;
    height: 640px;
    background: var(--card);
    overflow: hidden;
    box-shadow: 0 18px 40px rgba(60, 40, 80, 0.18);
  }
  .card-art {
    position: absolute;
    inset: 0;
    width: 1000px;
    height: 640px;
  }
  .brand {
    position: absolute;
    left: 66px;
    top: 200px;
    display: flex;
    align-items: center;
    gap: 18px;
    color: var(--ink);
    font-weight: 800;
  }
  .brand-dot {
    width: 54px;
    height: 54px;
    border-radius: 50%;
    background: var(--gold);
    flex: none;
  }
  .brand-name {
    font-size: 96px;
    line-height: 0.95;
    letter-spacing: -0.01em;
  }
  .brand-sector {
    display: block;
    font-size: 34px;
    letter-spacing: 0.28em;
    line-height: 1.3;
    padding-left: 6px;
  }
  .contact {
    position: absolute;
    left: 514px;
    top: 150px;
    width: 400px;
    text-align: center;
    color: var(--text);
  }
  .contact-name {
    color: var(--gold);
    font-size: 36px;
    font-weight: 500;
    letter-spacing: 0.01em;
  }
  .contact-role {
    margin-top: 6px;
    font-size: 34px;
    font-weight: 500;
    letter-spacing: 0.42em;
    padding-left: 0.42em;
    color: var(--ink);
  }
  .contact-rule {
    width: 94px;
    height: 4px;
    margin: 18px auto 40px;
    background: var(--gold);
  }
  .contact-line {
    font-size: 28px;
    line-height: 1.48;
  }
  .website {
    position: absolute;
    left: 0;
    right: 0;
    bottom: 10px;
    text-align: center;
    padding-left: 30px;
    color: var(--white);
    font-size: 29px;
    font-weight: 500;
  }
</style>
</head>
<body>
  <div class="business-card">
    <svg class="card-art" viewBox="0 0 1000 640" aria-hidden="false">
      <defs>
        <linearGradient id="swoosh" x1="0" y1="0" x2="1" y2="0">
          <stop offset="0" stop-color="#8a5a1c" stop-opacity="0"/>
          <stop offset="0.45" stop-color="#5a3510"/>
          <stop offset="1" stop-color="#000000"/>
        </linearGradient>
      </defs>
      <path role="img" aria-label="Faint sunburst emblem area" fill="var(--cream)"
            d="M690 0 H1000 V640 H455 C440 560 445 400 510 250 C560 130 620 50 690 0 Z"/>
      <path class="gold-band" fill="var(--gold)"
            d="M0 517 C180 555 330 575 520 572 C700 570 850 545 1000 510 V640 H0 Z"/>
      <path class="band-gap" fill="var(--white)"
            d="M470 566 C700 560 860 520 1000 468 V510 C850 545 700 570 520 572 Z"/>
      <path class="swoosh" fill="url(#swoosh)"
            d="M480 566 C700 555 860 500 1000 438 V500 C850 540 690 562 480 566 Z"/>
    </svg>

    <div class="brand">
      <span class="brand-dot"></span>
      <div>
        <span class="brand-name">Corra</span>
        <span class="brand-sector">OIL &amp; GAS</span>
      </div>
    </div>

    <div class="contact">
      <p class="contact-name">YOUR NAME</p>
      <p class="contact-role">OWNER</p>
      <div class="contact-rule"></div>
      <p class="contact-line">(555) 010-0000</p>
      <p class="contact-line">info@corra-energy.com</p>
      <p class="contact-line">your address</p>
    </div>

    <p class="website">www.corra-energy.com</p>
  </div>
</body>
</html>
```